Business Card Design

We have our logo and everything in place. Looking to have a layout for our new business cards designed. These will be printed with a matte finish, possibly rounded corners, and looking to incorporate some cool spot UV layers into the design.

Ive uploaded the existing card front and back as well as our logo.

Card Size Will Be 3.5" x 2"

```html
<!DOCTYPE html>
<html lang="en">
<head>
<meta charset="utf-8">
<title>Ridgeline Porch Works – Business Card</title>
<link href="https://fonts.googleapis.com/css2?family=Arimo:wght@400;700&display=swap" rel="stylesheet">
<style>
  :root {
    --backdrop: #3b3532;
    --card: #141414;
    --card-edge: #232323;
    --uv-mark: #8a8a8a;
    --uv-sheen: rgba(255, 255, 255, 0.07);
    --ink: #ffffff;
    --rule: #cfcfcf;
  }
  html, body {
    margin: 0;
    padding: 0;
    width: 1200px;
    height: 716px;
    overflow: hidden;
    background: var(--backdrop);
    font-family: "Arimo", Arial, sans-serif;
  }
  .canvas {
    position: relative;
    width: 1200px;
    height: 716px;
  }
  .card {
    position: absolute;
    top: 215px;
    width: 500px;
    height: 286px;
    background: var(--card);
    border: 1px solid var(--card-edge);
    border-radius: 10px;
    box-sizing: border-box;
    overflow: hidden;
  }
  .card--front { left: 70px; }
  .card--back { left: 630px; }

  /* spot UV gloss layer */
  .card__gloss {
    position: absolute;
    inset: 0;
    background: linear-gradient(125deg,
      transparent 20%,
      var(--uv-sheen) 42%,
      rgba(255, 255, 255, 0.12) 50%,
      var(--uv-sheen) 58%,
      transparent 80%);
    pointer-events: none;
  }
  .card--back .card__gloss {
    right: 268px;
  }

  .brand {
    display: flex;
    align-items: center;
    gap: 12px;
    color: var(--uv-mark);
    font-weight: 700;
    white-space: nowrap;
  }
  .brand__square {
    background: var(--uv-mark);
    flex: none;
  }
  .card--front .brand {
    position: absolute;
    inset: 0;
    justify-content: center;
    font-size: 30px;
  }
  .card--front .brand__square { width: 22px; height: 22px; }

  .card--back .brand {
    position: absolute;
    left: 0;
    width: 232px;
    top: 0;
    bottom: 0;
    justify-content: center;
    font-size: 16px;
    gap: 8px;
  }
  .card--back .brand__square { width: 12px; height: 12px; }

  .divider {
    position: absolute;
    left: 232px;
    top: 42px;
    width: 1px;
    height: 200px;
    background: var(--rule);
  }
  .contact {
    position: absolute;
    left: 233px;
    right: 0;
    top: 70px;
    color: var(--ink);
    text-align: center;
  }
  .contact__name {
    margin: 0;
    font-size: 22px;
    font-weight: 700;
    letter-spacing: 0.2px;
  }
  .contact__title {
    margin: 2px 0 0;
    font-size: 15px;
    font-weight: 700;
  }
  .contact__lines {
    list-style: none;
    margin: 34px 0 0;
    padding: 0;
    font-size: 14px;
    line-height: 24px;
    text-align: center;
  }
</style>
</head>
<body>
<main class="canvas">
  <section class="card card--front" aria-label="Card front">
    <div class="card__gloss"></div>
    <div class="brand">
      <span class="brand__square"></span>
      <span class="brand__name">Ridgeline Porch Works</span>
    </div>
  </section>

  <section class="card card--back" aria-label="Card back">
    <div class="card__gloss"></div>
    <div class="brand">
      <span class="brand__square"></span>
      <span class="brand__name">Ridgeline Porch Works</span>
    </div>
    <div class="divider"></div>
    <div class="contact">
      <h1 class="contact__name">Daniel Mercer</h1>
      <p class="contact__title">President</p>
      <ul class="contact__lines">
        <li class="phone">555.014.2738</li>
        <li>www.ridgelineporchworks.com</li>
        <li>hello@ridgelineporchworks.com</li>
      </ul>
    </div>
  </section>
</main>
</body>
</html>
```